Kestrel Ridgeway LLC stationery, business card and web page design.

i need a full set of stationery designed using the name "Kestrel Ridgeway LLC" with a tag line "construction consulting services". using the uploaded monkey icon as the logo.

i like the colors orange, green and black in general but im not limited to that. the company offers consulting services to various types of construction businesses.

Target Market(s)

i travel around the country in a 4x4 camper offering consulting services and technical training short term and long to various types of construction companies.

Industry/Entity Type

Construction Company

Contact Information for Business Card

Martin Hale
m.hale@kestrelridgeway.example
2475 Birchfield Rd
Bohemia, NY 11716
555 314 0627

list these services on the card.

Business Consulting
Capital Investments
Marketing Implementations
Technical Training

Number of Pages Required

1 page

Colors

Designer to choose colors to be used in the design.

Requirements
Must have
• company info and use of the monkey icon i provided.
Nice to have
• a fun but professional design
Should not have
• the color red

```html
<!DOCTYPE html>
<html lang="en">
<head>
<meta charset="utf-8">
<title>Kestrel Ridgeway LLC – Stationery</title>
<link href="https://fonts.googleapis.com/css2?family=Lato:wght@700&family=Montserrat:wght@400;500&display=swap" rel="stylesheet">
<style>
  :root {
    --orange: #F99B1A;
    --ink: #333333;
    --mark: #1E1E1E;
    --board: #BDB9B8;
    --paper: #FFFFFF;
    --ghost: #E2E2E2;
  }
  * { box-sizing: border-box; margin: 0; padding: 0; }
  html, body { width: 1200px; height: 1200px; overflow: hidden; }
  body { position: relative; background: var(--board); font-family: "Lato", sans-serif; }

  .banner {
    position: absolute; left: 0; top: 0; width: 1200px; height: 248px;
    background: var(--orange);
    box-shadow: 0 14px 14px rgba(0,0,0,.45);
  }

  .lockup { position: absolute; }
  .lockup .mark { position: absolute; border-radius: 50%; background: var(--mark); }
  .lockup .rule { position: absolute; background: var(--ink); }
  .lockup .name {
    position: absolute; font-weight: 700; color: var(--ink); line-height: 1; white-space: nowrap;
  }
  .lockup .tagline {
    position: absolute; font-family: "Montserrat", sans-serif; font-weight: 400;
    text-transform: uppercase; white-space: nowrap;
  }

  /* banner lockup */
  .banner .mark { left: 328px; top: 48px; width: 124px; height: 124px; }
  .banner .rule { left: 474px; top: 50px; width: 4px; height: 130px; }
  .banner .name { left: 505px; top: 56px; font-size: 58px; line-height: 64px; }
  .banner .tagline { left: 328px; top: 193px; font-size: 20px; letter-spacing: 4.6px; color: var(--paper); }

  .sheet {
    position: absolute; background: var(--paper); overflow: hidden;
    box-shadow: 8px 12px 14px rgba(0,0,0,.4);
  }
  .letterhead { left: 22px; top: 318px; width: 575px; height: 813px; }
  .card-front { left: 608px; top: 373px; width: 574px; height: 255px; background: var(--orange); }
  .card-back { left: 608px; top: 654px; width: 574px; height: 254px; }

  /* small lockups */
  .letterhead .mark { left: 44px; top: 36px; width: 68px; height: 68px; }
  .letterhead .rule { left: 122px; top: 42px; width: 2px; height: 66px; }
  .letterhead .name { left: 136px; top: 44px; font-size: 28px; line-height: 32px; }
  .letterhead .tagline { left: 46px; top: 115px; font-size: 10.5px; letter-spacing: 2.1px; color: var(--orange); }

  .card .mark { left: 196px; top: 97px; width: 46px; height: 46px; }
  .card .rule { left: 248px; top: 99px; width: 2px; height: 46px; }
  .card .name { left: 258px; top: 103px; font-size: 20px; line-height: 21px; }
  .card .tagline { left: 198px; top: 150px; font-size: 7px; letter-spacing: 1.3px; }
  .card-front .tagline { color: var(--ink); }
  .card-back .tagline { color: var(--orange); }
  .card-back .mark { top: 94px; }
  .card-back .rule { top: 96px; }
  .card-back .name { top: 100px; }
  .card-back .tagline { top: 146px; }

  .emblem { position: absolute; border-radius: 50%; }
  .letterhead .emblem { left: -120px; top: 270px; width: 490px; height: 520px; background: var(--ghost); }
  .card-front .emblem { left: 458px; top: 10px; width: 230px; height: 240px; background: var(--mark); }
  .card-back .emblem { left: -120px; top: 20px; width: 232px; height: 232px; background: var(--mark); }

  .contact {
    position: absolute; text-align: right; font-size: 8.5px; line-height: 12.5px;
    color: var(--ink); padding-right: 8px; border-right: 2px solid var(--mark);
    font-family: "Lato", sans-serif; font-weight: 400; list-style: none;
  }
  .letterhead .contact { right: 29px; top: 735px; }
  .card-back .contact { right: 22px; top: 188px; }
</style>
</head>
<body>

<header class="banner">
  <div class="lockup">
    <span class="mark" role="img" aria-label="Company emblem"></span>
    <span class="rule"></span>
    <h1 class="name">Kestrel<br>Ridgeway LLC</h1>
    <p class="tagline">Construction&nbsp; Consulting&nbsp; Services</p>
  </div>
</header>

<section class="sheet letterhead">
  <span class="emblem" role="img" aria-label="Large faint company emblem watermark"></span>
  <div class="lockup">
    <span class="mark" role="img" aria-label="Company emblem"></span>
    <span class="rule"></span>
    <h2 class="name">Kestrel<br>Ridgeway LLC</h2>
    <p class="tagline">Construction&nbsp; Consulting&nbsp; Services</p>
  </div>
  <ul class="contact">
    <li>yoursite.example</li>
    <li>name@yoursite.example</li>
    <li>123-123-1234 ( corporate)</li>
    <li>321-321-4321 (mobile )</li>
  </ul>
</section>

<section class="sheet card card-front">
  <span class="emblem" role="img" aria-label="Large company emblem cropped at right edge"></span>
  <div class="lockup">
    <span class="mark" role="img" aria-label="Company emblem"></span>
    <span class="rule"></span>
    <h2 class="name">Kestrel<br>Ridgeway LLC</h2>
    <p class="tagline">Construction&nbsp; Consulting&nbsp; Services</p>
  </div>
</section>

<section class="sheet card card-back">
  <span class="emblem" role="img" aria-label="Large company emblem cropped at left edge"></span>
  <div class="lockup">
    <span class="mark" role="img" aria-label="Company emblem"></span>
    <span class="rule"></span>
    <h2 class="name">Kestrel<br>Ridgeway LLC</h2>
    <p class="tagline">Construction&nbsp; Consulting&nbsp; Services</p>
  </div>
  <ul class="contact">
    <li>yoursite.example</li>
    <li>name@yoursite.example</li>
    <li>123-123-1234 ( corporate)</li>
    <li>321-321-4321 (mobile )</li>
  </ul>
</section>

</body>
</html>
```